Website Name Corvane Tally

I need a website called Corvane Tally:

This site is made for: Asking people to write via Call to Action/Email about their experience regarding procedures in beauty treatments cosmetic, aesthetic and plastic surgery and doctors, clinics and institutes in certain countries/counties/etc – good and bad.
We want to find the 5 best, the 5 worst, the most effective, most ineffective, most expensive, most useless procedures and doctors, clinics, cosmetic institutes. We want to rank them and display the good and the bad, and we want to build a site which will be the base for our future projects in digital marketing for clinics, institutes and doctors. We want to build traffic, want to get data via opt in and of course we want personal opinions to feed a review site.

No complicated website just clear and easy to operate. It has to be catchy though. We are looking for a lot of traffic and we want to generate a lot of data which we want to use for future projects.

attached as word document you will find more details

```html
<!DOCTYPE html>
<html lang="en">
<head>
<meta charset="utf-8">
<title>Corvane Tally</title>
<link rel="stylesheet" href="https://fonts.googleapis.com/css2?family=Jost:ital,wght@0,300;0,400;0,500;1,400&family=Montserrat:wght@400;500;600&family=Lato:wght@400;700&display=swap">
<style>
  :root {
    --ink: #1f1f1f;
    --ink-soft: #444;
    --muted: #6b6b6b;
    --btn: #2a2a2a;
    --row: #f7f7f7;
    --row-num: #efefef;
    --accent-num: #3a3aff;
    --star: #f2b01e;
    --footer: #2b2b2b;
    --footer-line: #444;
    --white: #fff;
  }
  * { box-sizing: border-box; margin: 0; padding: 0; }
  html, body { width: 1200px; height: 3581px; overflow: hidden; }
  body { position: relative; background: var(--white); color: var(--ink); font-family: "Jost", sans-serif; }
  .abs { position: absolute; }

  .site-header { position: absolute; top: 0; left: 0; width: 1200px; height: 96px; background: var(--white); }
  .brand { position: absolute; left: 111px; top: 30px; font: 400 29px "Jost", sans-serif; letter-spacing: .5px; color: var(--ink); }
  .menu-toggle { position: absolute; left: 1055px; top: 36px; width: 32px; height: 24px; }
  .menu-toggle span { display: block; height: 4px; background: var(--ink); border-radius: 2px; margin-bottom: 6px; }

  .hero { position: absolute; top: 96px; left: 0; width: 1200px; height: 625px;
    background: linear-gradient(90deg, #e8e2de 0%, #ddd3cd 40%, #d3b8a6 65%, #caa792 85%, #d9c3b4 100%); }
  .hero-title { position: absolute; left: 111px; top: 120px; font: 300 64px/86px "Jost", sans-serif; color: #2a2a2a; letter-spacing: 1px; }
  .hero-sub { position: absolute; left: 115px; top: 300px; font: 400 20px/34px "Montserrat", sans-serif; color: #2a2a2a; }
  .btn { display: inline-flex; align-items: center; justify-content: center; background: var(--btn); color: var(--white);
    font: 500 17px "Montserrat", sans-serif; text-transform: uppercase; }
  .hero .btn { position: absolute; left: 115px; top: 435px; width: 134px; height: 56px; }
  .slider-dots { position: absolute; top: 575px; left: 570px; display: flex; gap: 10px; }
  .slider-dots i { width: 7px; height: 7px; border-radius: 50%; background: #9a9a9a; }
  .slider-dots i.on { background: #222; }

  .about-photo { position: absolute; left: 97px; top: 831px; width: 477px; height: 465px; border: 2px solid #222;
    background: linear-gradient(135deg, #f2f2f2 0%, #e6e6e6 45%, #c9a58d 60%, #ececec 100%); }
  .about-title { position: absolute; left: 633px; top: 838px; font: 300 66px/86px "Jost", sans-serif; color: var(--ink); }
  .about-text { position: absolute; left: 633px; top: 1026px; width: 470px; font: 400 16px/25.6px "Montserrat", sans-serif; color: var(--ink-soft); }
  .about .btn { position: absolute; left: 633px; top: 1214px; width: 148px; height: 55px; }

  .section-title { position: absolute; left: 0; width: 1200px; text-align: center; font: 300 50px "Jost", sans-serif; color: var(--ink); }

  .accordion { position: absolute; left: 111px; top: 1518px; width: 977px; }
  .acc-row { display: flex; background: var(--row); margin-bottom: 7px; height: 63px; }
  .acc-row.open { height: 146px; }
  .acc-num { width: 69px; background: var(--row-num); border-right: 2px solid #e2e2e2; font: 600 18px "Montserrat", sans-serif;
    text-align: center; padding-top: 21px; }
  .acc-row.open .acc-num { color: var(--accent-num); }
  .acc-body { padding: 18px 0 0 34px; font: 400 21px "Jost", sans-serif; letter-spacing: .5px; color: var(--muted); }
  .acc-row.open .acc-body { color: var(--ink); }
  .acc-body .btn { margin-top: 22px; width: 167px; height: 54px; font-size: 16px; }

  .topics-title { position: absolute; top: 2151px; left: 0; width: 1200px; text-align: center; font: 500 48px "Montserrat", sans-serif; color: var(--ink); }
  .topic { position: absolute; top: 2242px; width: 307px; }
  .topic-photo { width: 307px; height: 274px; }
  .topic-name { margin-top: 28px; font: 300 27px/39px "Jost", sans-serif; color: #333; }

  .reviews { position: absolute; top: 2688px; left: 0; width: 1200px; height: 515px;
    background: linear-gradient(90deg, #ecebea 0%, #f1efee 50%, #e9e7e5 100%); }
  .quote-mark { position: absolute; font: 400 200px/1 "Jost", sans-serif; color: #d6d4d2; }
  .reviews .section-title { top: 72px; font-size: 50px; }
  .stars { position: absolute; top: 164px; left: 0; width: 1200px; text-align: center; color: var(--star); font-size: 17px; letter-spacing: 1px; }
  .review-text { position: absolute; top: 198px; left: 180px; width: 840px; text-align: center; font: italic 400 17px/30px "Lato", sans-serif; color: #444; }
  .reviewer { position: absolute; top: 342px; left: 0; width: 1200px; text-align: center; font: 600 17px "Montserrat", sans-serif; }
  .reviewer-role { position: absolute; top: 372px; left: 0; width: 1200px; text-align: center; font: 400 17px "Jost", sans-serif; color: #444; }
  .review-dots { position: absolute; top: 428px; left: 548px; display: flex; gap: 16px; }
  .review-dots i { width: 24px; height: 4px; background: #cfcfcf; }
  .review-dots i.on { background: #222; }

  .site-footer { position: absolute; top: 3203px; left: 0; width: 1200px; height: 378px; background: var(--footer); color: var(--white); font-family: "Lato", sans-serif; }
  .footer-brand { position: absolute; left: 111px; top: 107px; font: 400 29px "Jost", sans-serif; }
  .socials { position: absolute; left: 111px; top: 171px; display: flex; gap: 3px; }
  .socials span { width: 45px; height: 45px; border: 1.5px solid var(--white); border-radius: 50%; }
  .footer-col { position: absolute; top: 103px; }
  .footer-col h3 { font: 700 18px "Montserrat", sans-serif; margin-bottom: 22px; letter-spacing: .3px; }
  .footer-col li { list-style: none; font-size: 15px; line-height: 25.5px; }
  .contact-item { display: flex; gap: 14px; font-size: 15px; line-height: 23px; margin-bottom: 12px; }
  .contact-item svg { flex: none; margin-top: 4px; }
  .newsletter { display: flex; width: 225px; height: 40px; border-radius: 4px; overflow: hidden; }
  .newsletter span { flex: 1; background: var(--white); color: #888; font-size: 15px; padding: 10px 13px; }
  .newsletter b { width: 54px; background: #a4a4a4; display: flex; align-items: center; justify-content: center; }
  .footer-rule { position: absolute; left: 111px; top: 307px; width: 977px; height: 1px; background: var(--footer-line); }
  .copyright { position: absolute; top: 330px; left: 0; width: 1200px; text-align: center; font-size: 15px; }
</style>
</head>
<body>

<header class="site-header">
  <div class="brand">CORVANE TALLY</div>
  <div class="menu-toggle" aria-label="Menu"><span></span><span></span><span></span></div>
</header>

<section class="hero">
  <div class="abs" style="inset:0" role="img" aria-label="Close-up portrait of a woman with fringe, soft skin tones"></div>
  <h1 class="hero-title">LOOK GOOD<br>FEEL GOOD</h1>
  <p class="hero-sub">SHARE YOUR AESTHETIC SURGERY,<br>PLASTIC SURGERY,COSMETIC MEDICAL<br>EXPERIENCES WITH US</p>
  <a class="btn">Contact</a>
  <div class="slider-dots"><i class="on"></i><i></i><i></i><i></i></div>
</section>

<section class="about">
  <div class="about-photo" role="img" aria-label="Woman seated on a bright studio floor"></div>
  <h2 class="about-title">ABOUT<br>CORVANE TALLY</h2>
  <p class="about-text">Lorem ipsum dolor sit amet, consectetur adipiscing elit, sed do eiusmod tempor incididunt ut labore et dolore magna aliqua. Ut enim ad minim veniam, quis nostrud exercitation ullamco laboris nisi ut aliquip ex ea commodo consequat. Duis aute irure dolor in reprehenderit in voluptate velit esse cillum dolore eu fugiat nulla pariatur.</p>
  <a class="btn">Learn More</a>
</section>

<h2 class="section-title" style="top:1408px">WRITE US YOUR EXPERIENCE</h2>
<div class="accordion">
  <div class="acc-row"><div class="acc-num">1</div><div class="acc-body">Write us your experience of best</div></div>
  <div class="acc-row open"><div class="acc-num">2</div><div class="acc-body">Write us your experience of worst<br><a class="btn">See Our Views</a></div></div>
  <div class="acc-row"><div class="acc-num">3</div><div class="acc-body">Write us your experience of most effective</div></div>
  <div class="acc-row"><div class="acc-num">4</div><div class="acc-body">Write us your experience of most useless</div></div>
  <div class="acc-row"><div class="acc-num">5</div><div class="acc-body">Write us your experience of most expensive procedure</div></div>
  <div class="acc-row"><div class="acc-num">6</div><div class="acc-body">Write us your experience of what you paid for</div></div>
  <div class="acc-row"><div class="acc-num">7</div><div class="acc-body">Write us your experience of who did the procedure</div></div>
</div>

<h2 class="topics-title">OUR TOPICS</h2>
<article class="topic" style="left:111px">
  <div class="topic-photo" role="img" aria-label="Portrait of a woman with natural makeup" style="background:linear-gradient(180deg,#ece6e2,#e3cfc4)"></div>
  <h3 class="topic-name">Aesthetic Medicine<br>Treatments</h3>
</article>
<article class="topic" style="left:446px">
  <div class="topic-photo" role="img" aria-label="Woman touching her forehead" style="background:linear-gradient(180deg,#e9d6c9,#f2e6de)"></div>
  <h3 class="topic-name">Medical Cosmetic<br>Treatments</h3>
</article>
<article class="topic" style="left:781px">
  <div class="topic-photo" role="img" aria-label="Laughing woman with red hair in a black top" style="background:linear-gradient(180deg,#ebe3e3,#b36a4e 55%,#2b2727)"></div>
  <h3 class="topic-name">Aesthetic &amp; Plastic<br>Surgery</h3>
</article>

<section class="reviews">
  <div class="abs" style="inset:0" role="img" aria-label="Faded portrait background"></div>
  <div class="quote-mark" style="left:106px;top:90px">&ldquo;</div>
  <div class="quote-mark" style="left:958px;top:305px">&rdquo;</div>
  <h2 class="section-title">OUR REVIEWS</h2>
  <div class="stars">★★★★★</div>
  <p class="review-text">Lorem ipsum dolor sit amet, consectetur adipiscing elit, sed do eiusmod tempor incididunt ut labore et dolore magna aliqua. Ut enim ad minim veniam, quis nostrud exercitation ullamco laboris nisi ut aliquip ex ea commodo consequat.Duis aute irure dolor in reprehenderit in voluptate velit esse cillum dolore eu fugiat nulla pariatur.</p>
  <div class="reviewer">MARA QUILL</div>
  <div class="reviewer-role">Lorem ipsum dolor</div>
  <div class="review-dots"><i></i><i class="on"></i><i></i></div>
</section>

<footer class="site-footer">
  <div class="footer-brand">CORVANE TALLY</div>
  <div class="socials"><span aria-label="Social link"></span><span aria-label="Social link"></span><span aria-label="Social link"></span><span aria-label="Social link"></span></div>

  <div class="footer-col" style="left:368px">
    <h3>QUICK LINKS</h3>
    <ul><li>Terms and Conditions</li><li>Privacy &amp; Cookie Polica</li><li>DSVGO Site</li></ul>
  </div>

  <div class="footer-col" style="left:587px">
    <h3>CONTACT US</h3>
    <div class="contact-item">
      <svg width="16" height="20" viewBox="0 0 16 20"><path d="M8 0a8 8 0 0 0-8 8c0 6 8 12 8 12s8-6 8-12a8 8 0 0 0-8-8zm0 11a3 3 0 1 1 0-6 3 3 0 0 1 0 6z" fill="#fff"/></svg>
      <span>Lorem ipsum dolor sit<br>amet, consectetur</span>
    </div>
    <div class="contact-item">
      <svg width="17" height="17" viewBox="0 0 24 24"><path d="M6.6 10.8a15 15 0 0 0 6.6 6.6l2.2-2.2a1 1 0 0 1 1-.25 11.4 11.4 0 0 0 3.6.6 1 1 0 0 1 1 1V20a1 1 0 0 1-1 1A17 17 0 0 1 3 4a1 1 0 0 1 1-1h3.5a1 1 0 0 1 1 1c0 1.25.2 2.45.6 3.6a1 1 0 0 1-.25 1z" fill="#fff"/></svg>
      <span>+1 (555) 014 2290</span>
    </div>
    <div class="contact-item">
      <svg width="18" height="14" viewBox="0 0 18 14"><rect width="18" height="14" rx="1.5" fill="#fff"/><path d="M1 1.5l8 6 8-6" stroke="#2b2b2b" stroke-width="1.6" fill="none"/></svg>
      <span>info@corvanetally.com</span>
    </div>
  </div>

  <div class="footer-col" style="left:859px">
    <h3>NEWSLETTER</h3>
    <div class="newsletter">
      <span>Enter email</span>
      <b><svg width="16" height="12" viewBox="0 0 18 14"><rect width="18" height="14" rx="1.5" fill="#fff"/><path d="M1 1.5l8 6 8-6" stroke="#a4a4a4" stroke-width="1.6" fill="none"/></svg></b>
    </div>
  </div>

  <div class="footer-rule"></div>
  <p class="copyright">©Copyrights 2023 Corvane Tally &nbsp;| &nbsp; All Rights Reserved</p>
</footer>

</body>
</html>
```